Fennick Executive Search - New Business Card Design Project

We are an executive search firm called Fennick Executive Search based in the UK. We require a custom design for a business card. We're looking to convey a professional service to executives for executive search recruitment services. In terms of colours, we like dark blues and grays (maybe even silver incorporated somewhere if we go for a foiled type of card) but we're open to your artistic flare. See our current logo in attachments. We are totally open on design so long as the design is slick and professional.
Updates

Thanks for all your contributions of various designs. I have to say the quality of work has been amazing which is going to make our job quite difficult in the coming days on making a decision. Thanks to you all that have taken the time to submit designs thus far. We'll keep on reviewing and try to narrow down our selection as soon as possible.

Target Market(s)

Executive Search

Industry/Entity Type

Recruitment

Contact Information for Business Card

Fennick Executive Search,
Discreetly Finding & Placing Senior Leaders
Gordon Pellbury, Managing Director,
07823 906417
0117 486 7132
gordon@fennickexecutive.co.uk
fennickexecutive.co.uk
58 Lindmoor Court, Hatherley Road, Bristol, BS32 9QJ

Font styles to use
Sans Serif
Other font styles liked:
• Roboto (which is used in our logo)

Requirements
Must have
• Our logo (It has a subtle fade on it from #02071d at top to #333649 at bottom)
• The logo can be on one side or both sides
• Must be elegant and professional
• We have 2nd slogan ADVISE | ENGAGE | REFINE | SECURE which can be incorporated into the card
Nice to have
• Use of blues and grey colours
• Compatible with similar styling to our website fennickexecutive.co.uk
Should not have
• Must not be overly brash
• Must not contain cartoon characters

```html
<!DOCTYPE html>
<html lang="en">
<head>
<meta charset="utf-8">
<title>Fennick Executive Search – Business Card</title>
<link rel="stylesheet" href="https://fonts.googleapis.com/css2?family=Open+Sans:wght@400;600;700&display=swap">
<style>
  :root {
    --bg: #e6e6e3;
    --navy: #12162e;
    --navy-ink: #171c3a;
    --silver: #b9b9b9;
    --silver-dim: #8e8e8e;
    --paper: #fbfbfa;
    --text: #1b1f3b;
  }
  * { box-sizing: border-box; margin: 0; padding: 0; }
  html, body {
    width: 1200px; height: 1200px; overflow: hidden;
    background: var(--bg);
    font-family: "Open Sans", sans-serif;
  }
  .canvas {
    width: 1200px; height: 1200px;
    display: flex; flex-direction: column; align-items: center; justify-content: center;
    gap: 70px;
  }
  .card {
    width: 840px; height: 480px; position: relative;
    box-shadow: 0 10px 30px rgba(0,0,0,.18);
  }
  /* Front */
  .card--front { background: var(--navy); }
  .front-brand {
    position: absolute; left: 120px; top: 150px;
    color: var(--silver);
  }
  .brand-name {
    font-weight: 600; font-size: 44px; letter-spacing: 1px;
    text-transform: uppercase; line-height: 1.1;
  }
  .brand-tagline {
    font-size: 19px; margin-top: 8px; color: var(--silver-dim);
  }
  .front-slogan {
    position: absolute; left: 120px; top: 310px;
    font-size: 21px; letter-spacing: .5px; color: var(--silver-dim);
  }
  /* Back */
  .card--back { background: var(--paper); color: var(--text); }
  .back-brand {
    position: absolute; right: 60px; top: 60px;
    font-weight: 600; font-size: 26px; text-transform: uppercase;
    letter-spacing: .5px; color: var(--navy-ink); text-align: right; line-height: 1.1;
  }
  .person {
    position: absolute; left: 55px; top: 150px;
    padding-left: 20px; border-left: 12px solid var(--navy-ink);
  }
  .person-name { font-size: 34px; line-height: 1.05; font-weight: 400; }
  .person-name strong { font-weight: 700; }
  .person-role { font-size: 17px; margin-top: 2px; }
  .contacts {
    position: absolute; left: 58px; top: 265px;
    list-style: none; font-size: 17px;
  }
  .contacts li { display: flex; align-items: center; gap: 14px; height: 27px; }
  .contacts svg { width: 16px; height: 16px; fill: var(--navy-ink); flex: none; }
  .divider { position: absolute; left: 0; top: 392px; width: 840px; height: 14px; }
  .website {
    position: absolute; left: 58px; top: 420px; font-size: 21px;
  }
</style>
</head>
<body>
<main class="canvas">
  <section class="card card--front">
    <div class="front-brand">
      <div class="brand-name">Fennick<br>Executive Search</div>
      <div class="brand-tagline">Discreetly Finding &amp; Placing Senior Leaders</div>
    </div>
    <div class="front-slogan">ADVISE | ENGAGE | REFINE | SECURE</div>
  </section>

  <section class="card card--back">
    <div class="back-brand">Fennick<br>Executive Search</div>
    <div class="person">
      <div class="person-name">Gordon <strong>Pellbury</strong></div>
      <div class="person-role">Managing Director</div>
    </div>
    <ul class="contacts">
      <li><svg viewBox="0 0 16 16"><path d="M2 5c0-2 2-3 6-3s6 1 6 3v1h-3V5H5v1H2z M4 7h8l2 6H2z"/></svg>07823 906417</li>
      <li><svg viewBox="0 0 16 16"><path d="M2 5c0-2 2-3 6-3s6 1 6 3v1h-3V5H5v1H2z M4 7h8l2 6H2z"/></svg>0117 486 7132</li>
      <li><svg viewBox="0 0 16 16"><path d="M1 3h14v10H1z M2 4l6 5 6-5" fill="none" stroke="#171c3a" stroke-width="1.6"/></svg>gordon@fennickexecutive.co.uk</li>
      <li><svg viewBox="0 0 16 16"><path d="M8 1a5 5 0 0 0-5 5c0 4 5 9 5 9s5-5 5-9a5 5 0 0 0-5-5zm0 7a2 2 0 1 1 0-4 2 2 0 0 1 0 4z"/></svg>58 Lindmoor Court, Hatherley Road, Bristol, BS32 9QJ</li>
    </ul>
    <svg class="divider" viewBox="0 0 840 14" aria-hidden="true">
      <path d="M0 12 H620 L630 4 H840 V13 H0 Z" fill="#171c3a"/>
      <rect x="0" y="11" width="840" height="2" fill="#171c3a"/>
    </svg>
    <div class="website">fennickexecutive.co.uk</div>
  </section>
</main>
</body>
</html>
```